Brookfarrow Osteopathy and dry needling business card

Business card for Brookfarrow Osteopathy and Dry Needling.

Industry/Entity Type

Health

Contact Information for Business Card

I do not have a phone number yet. I also do not have an email address yet. The physical address is: 48 Lower Crane Street Brookfarrow The website is: www.brookfarrowosteosteopathy.example My details are: Dr Martin Pellowe, Osteopath (B.Clin.Sci (Ost) M.Ost BSC ECON (Hons)

Colors
0094D4
00A9DD
6FCCEA
C7EBF8
E9F6FB

Requirements
Must have
• logo on the back
Nice to have
• Maybe a space for me to write an appointment time and date on the card.

```html
<!DOCTYPE html>
<html lang="en">
<head>
<meta charset="utf-8">
<title>Brookfarrow Osteopathy and Dry Needling – Business Card</title>
<link rel="stylesheet" href="https://fonts.googleapis.com/css2?family=Montserrat:wght@400;500;700&display=swap">
<style>
  :root {
    --brand-blue: #0094D4;
    --brand-sky: #00A9DD;
    --brand-light: #6FCCEA;
    --brand-pale: #C7EBF8;
    --brand-mist: #E9F6FB;
    --accent-orange: #F7943A;
    --ink: #1f1f1f;
    --paper: #ffffff;
    --backdrop: #e4e7ea;
  }
  * { box-sizing: border-box; margin: 0; padding: 0; }
  html, body { width: 1200px; height: 1186px; overflow: hidden; }
  body {
    background: var(--backdrop);
    font-family: "Montserrat", sans-serif;
    position: relative;
  }
  .card {
    position: absolute;
    left: 130px;
    width: 940px;
    height: 537px;
    overflow: hidden;
    box-shadow: 0 6px 18px rgba(0,0,0,.18);
  }
  /* Back */
  .card-back { top: 40px; background: var(--brand-blue); color: var(--paper); }
  .back-mark {
    position: absolute; left: 320px; top: 55px;
    width: 300px; height: 300px;
    border: 4px solid var(--paper); border-radius: 50%;
    display: flex; align-items: center; justify-content: center;
    text-align: center;
  }
  .mark-name {
    font-weight: 700; font-size: 24px; line-height: 1.25;
    letter-spacing: 1px; text-transform: uppercase;
  }
  .appointment {
    position: absolute; left: 60px; right: 60px; bottom: 70px;
    display: flex; gap: 24px; font-size: 22px; font-weight: 500;
  }
  .appointment .field { display: flex; align-items: flex-end; flex: 1; }
  .appointment .field.date { flex: 0.8; }
  .appointment .dots {
    flex: 1; margin-left: 6px; margin-bottom: 5px;
    border-bottom: 2px dotted var(--paper);
  }
  /* Front */
  .card-front { top: 609px; background: var(--paper); }
  .front-mark {
    position: absolute; left: 55px; top: 70px;
    width: 270px; height: 270px;
    border: 4px solid var(--brand-sky); border-radius: 50%;
    display: flex; align-items: center; justify-content: center; text-align: center;
  }
  .front-mark .mark-name { color: var(--brand-sky); font-size: 22px; }
  .divider {
    position: absolute; left: 360px; top: 80px; width: 2px; height: 260px;
    background: var(--brand-sky);
  }
  .details { position: absolute; left: 395px; top: 95px; color: var(--ink); }
  .person-name { color: var(--brand-blue); font-size: 40px; font-weight: 700; margin-bottom: 12px; }
  .credentials { font-size: 22px; line-height: 1.4; margin-bottom: 14px; }
  .contact-list { list-style: none; font-size: 22px; line-height: 1.55; }
  .contact-list li { display: flex; align-items: center; gap: 14px; }
  .contact-list svg { width: 20px; height: 20px; flex: none; }
  .address-band {
    position: absolute; left: 0; right: 0; top: 392px; height: 70px;
    background: var(--brand-blue); color: var(--paper);
    display: flex; align-items: center; padding-left: 150px; gap: 14px;
    font-size: 26px; font-weight: 500;
  }
  .address-band svg { width: 22px; height: 28px; fill: var(--paper); }
  .accent-strip {
    position: absolute; right: 0; top: 352px; width: 200px; height: 40px;
    background: var(--accent-orange);
  }
  .corner-badge {
    position: absolute; left: 700px; top: 342px; width: 62px; height: 62px;
    border-radius: 50%; background: var(--brand-mist); border: 3px solid var(--paper);
  }
</style>
</head>
<body>
  <section class="card card-back" aria-label="Card back">
    <div class="back-mark">
      <span class="mark-name">Brookfarrow<br>Osteopathy<br>&amp; Dry Needling</span>
    </div>
    <div class="appointment">
      <div class="field"><span>Appointment Time</span><span class="dots"></span></div>
      <div class="field date"><span>Date</span><span class="dots"></span></div>
    </div>
  </section>

  <section class="card card-front" aria-label="Card front">
    <div class="front-mark">
      <span class="mark-name">Brookfarrow<br>Osteopathy<br>&amp; Dry Needling</span>
    </div>
    <div class="divider"></div>
    <div class="details">
      <h1 class="person-name">Dr. Martin Pellowe</h1>
      <p class="credentials">Osteopath (B.Clin.Sci (Ost)<br>M.Ost BSC ECON (Hons)</p>
      <ul class="contact-list">
        <li><svg viewBox="0 0 24 24"><circle cx="12" cy="12" r="10" fill="#0094D4"/><path d="M2 12h20M12 2c3 3 3 17 0 20M12 2c-3 3-3 17 0 20" stroke="#fff" stroke-width="1.5" fill="none"/></svg>www.brookfarrowosteosteopathy.example</li>
      </ul>
    </div>
    <div class="accent-strip"></div>
    <div class="address-band">
      <svg viewBox="0 0 24 30"><path d="M12 0a11 11 0 0 0-11 11c0 8 11 19 11 19s11-11 11-19A11 11 0 0 0 12 0zm0 15a4 4 0 1 1 0-8 4 4 0 0 1 0 8z"/></svg>
      <span>48 Lower Crane Street Brookfarrow</span>
    </div>
    <div class="corner-badge"></div>
  </section>
</body>
</html>
```